Modern Spot UV Business Card design

We are a relatively new real estate agency. We need a business card that reflects the professionalism and prestige of our company but is also modern and fresh, based around our logo.
We would love to utilise spot UV.
Happy to let the designers use their imagination and see what they come up with (we're not very creative, so have no ideas for you, sorry) :-)
We'd like one for each staff member, but I've just provided one staff members photo here to avoid confusion.

Target Market(s)

Families

Industry/Entity Type

Real Estate Agent

Contact Information for Business Card

Colin Varga - Director & Principal
Mobile: 0491 527 806
Email: colin.varga@vbrokers.example.com.au
Phone: (08) 7364 9150
Fax: (08) 7364 9182
www.vargabrokersrealestate.example.com.au

Font styles to use
Other font styles liked:
• Kabel Dm BT

Requirements
Must have
• Contact details, logo, photo, spot UV
Nice to have
• Modern interesting features that will make people comment. Nothing too feminine nor too masculine.
Should not have
• No houses! Nothing typical of a real estate agent.

```html
<!DOCTYPE html>
<html lang="en">
<head>
<meta charset="utf-8">
<title>Colin Varga – Business Card</title>
<link rel="stylesheet" href="https://fonts.googleapis.com/css2?family=Josefin+Sans:wght@700&display=swap">
<style>
  :root {
    --cream: #f5f5cc;
    --green: #006b3a;
    --gold: #b18e4d;
    --gold-light: #c9a66b;
    --gold-mid: #b39559;
    --burgundy: #7a0d12;
    --white: #ffffff;
    --shadow: rgba(60, 50, 30, 0.45);
  }
  html, body {
    margin: 0;
    padding: 0;
    overflow: hidden;
    background: var(--cream);
  }
  .card {
    position: relative;
    width: 1200px;
    height: 688px;
    background: var(--cream);
    overflow: hidden;
  }
  .card__waves {
    position: absolute;
    inset: 0;
    width: 1200px;
    height: 688px;
  }
  .wave-green { fill: var(--green); }
  .wave-edge { fill: none; stroke: var(--white); stroke-width: 6; }
  .wave-stripe { fill: var(--gold); }
  .contact {
    position: absolute;
    left: 0;
    right: 0;
    top: 278px;
    text-align: center;
    font-family: "Josefin Sans", sans-serif;
    font-weight: 700;
    line-height: 1;
    text-shadow: 3px 3px 3px var(--shadow);
  }
  .contact p { margin: 0; }
  .contact__name { font-size: 46px; color: var(--gold-light); margin-bottom: 16px; }
  .contact__title { font-size: 40px; color: var(--burgundy); margin-bottom: 17px; }
  .contact__mobile { font-size: 40px; color: var(--gold-mid); margin-bottom: 12px; }
  .contact__email { font-size: 38px; color: var(--burgundy); }
</style>
</head>
<body>
<main class="card">
  <svg class="card__waves" viewBox="0 0 1200 688" aria-hidden="true">
    <g class="wave-set wave-set--top">
      <path class="wave-green" d="M0,0 H1172 C940,110 560,170 0,125 Z"/>
      <path class="wave-edge" d="M1172,0 C940,110 560,170 330,150"/>
      <path class="wave-stripe" d="M0,138 C320,178 720,178 1200,66 L1200,98 C720,208 320,200 0,160 Z"/>
    </g>
    <g class="wave-set wave-set--bottom" transform="rotate(180 600 344)">
      <path class="wave-green" d="M0,0 H1172 C940,110 560,170 0,125 Z"/>
      <path class="wave-edge" d="M1172,0 C940,110 560,170 330,150"/>
      <path class="wave-stripe" d="M0,138 C320,178 720,178 1200,66 L1200,98 C720,208 320,200 0,160 Z"/>
    </g>
  </svg>
  <section class="contact">
    <p class="contact__name">Colin Varga</p>
    <p class="contact__title">Director &amp; Principal</p>
    <p class="contact__mobile">Cell: 0491 527 806</p>
    <p class="contact__email">colin.varga@vbrokers.example.com.au</p>
  </section>
</main>
</body>
</html>
```